Boring Fiberglass Repair Company needs creative business cards

The Fiberglass Repair industry isn't very fun or creative but we'd like a business card that communicates a fresh, modern, and service-oriented feel. We repair bathroom fixtures (bath tubs, showers, etc) which are made out of fiberglass. Our fiberglass repair service will be sold to bathtub manufacturers and also businesses that sell bathtubs. We will also offer our services to home owners that have broken showers and bathtubs.
Target Market(s)
Home builders, plumbing wholesalers, home owners
Contact Information for Business Card
Name
Phone Number
Email Address
Business Address
Tag line: "Quality Craftsmanship Today"

```html
<!DOCTYPE html>
<html lang="en">
<head>
<meta charset="utf-8">
<title>Mesa Ridge Fiberglass – Business Cards</title>
<link rel="stylesheet" href="https://fonts.googleapis.com/css2?family=Montserrat:wght@400;500;700;800&family=Lato:wght@700&display=swap">
<style>
  :root {
    --bg: #e4e4e4;
    --navy-deep: #0c1631;
    --navy-brand: #1e2d5e;
    --red: #e31e24;
    --white: #ffffff;
    --text-light: #f2f3f7;
    --shadow: 0 14px 30px rgba(0,0,0,0.18);
  }
  * { box-sizing: border-box; margin: 0; padding: 0; }
  html, body { width: 1200px; height: 800px; overflow: hidden; }
  body {
    background: var(--bg);
    font-family: "Montserrat", sans-serif;
    position: relative;
  }
  .card {
    position: absolute;
    top: 245px;
    width: 540px;
    height: 310px;
    box-shadow: var(--shadow);
    overflow: hidden;
  }
  /* Back side */
  .card--back { left: 40px; background: var(--navy-deep); }
  .brand-band {
    position: absolute; left: 0; top: 0; bottom: 0;
    width: 118px;
    background: var(--white);
    border-right: 3px solid var(--red);
    display: flex; align-items: center; justify-content: center;
  }
  .brand-band .brand-name {
    transform: rotate(-90deg);
    white-space: nowrap;
    text-align: center;
  }
  .brand-name {
    font-family: "Montserrat", sans-serif;
    font-weight: 800;
    color: var(--navy-brand);
    line-height: 1;
  }
  .brand-band .brand-main { font-size: 27px; letter-spacing: 0.5px; }
  .brand-band .brand-sub { font-size: 13px; letter-spacing: 10px; margin-top: 6px; margin-right: -10px; }

  .details {
    position: absolute; left: 150px; top: 32px; right: 24px;
    color: var(--text-light);
  }
  .person-name { font-size: 26px; font-weight: 700; line-height: 32px; }
  .person-name .first { color: var(--red); }
  .person-title { font-size: 14px; font-weight: 500; line-height: 18px; margin-bottom: 12px; }
  .address { font-size: 13px; line-height: 17px; margin-bottom: 10px; }
  .contact-list { list-style: none; font-size: 12.5px; line-height: 18px; }
  .contact-list li { display: flex; align-items: center; gap: 8px; }
  .contact-list svg { width: 11px; height: 11px; flex: none; }
  .divider { width: 200px; height: 1.5px; background: var(--red); margin: 8px 0 4px; }
  .services-label { color: var(--red); font-size: 14px; font-weight: 700; line-height: 19px; }
  .services-list { list-style: none; font-size: 12.5px; line-height: 17px; }
  .services-list li { display: flex; align-items: center; gap: 9px; }
  .services-list li::before {
    content: ""; width: 5px; height: 5px; border-radius: 50%; background: var(--red);
  }
  .accent-line { position: absolute; inset: 0; pointer-events: none; }

  /* Front side */
  .card--front {
    left: 620px; background: var(--white);
    display: flex; flex-direction: column; align-items: center; justify-content: center;
  }
  .card--front .brand-name { text-align: center; margin-top: -10px; }
  .card--front .brand-main { font-size: 44px; letter-spacing: 1px; }
  .card--front .brand-sub { font-size: 18px; letter-spacing: 16px; margin-top: 8px; margin-right: -16px; }
  .tagline {
    font-family: "Lato", sans-serif; font-weight: 700;
    color: var(--navy-brand); font-size: 17px; margin-top: 48px;
  }
</style>
</head>
<body>

<section class="card card--back" aria-label="Business card, contact side">
  <svg class="accent-line" viewBox="0 0 540 310" aria-hidden="true">
    <line x1="300" y1="310" x2="540" y2="90" stroke="#1a2748" stroke-width="1.5"/>
  </svg>
  <div class="brand-band">
    <div class="brand-name">
      <div class="brand-main">MESA RIDGE</div>
      <div class="brand-sub">FIBERGLASS</div>
    </div>
  </div>
  <div class="details">
    <h1 class="person-name"><span class="first">Adrian</span> Kessler</h1>
    <p class="person-title">President</p>
    <p class="address">2210 Harbor Lane,<br>Suite 14</p>
    <ul class="contact-list">
      <li>
        <svg viewBox="0 0 12 12" aria-hidden="true"><path fill="#e31e24" d="M2.3 1l1.9 0 .8 2.4-1.2.9a6 6 0 0 0 3.3 3.3l.9-1.2 2.4.8v1.9c0 .6-.5 1-1.1 1A9.5 9.5 0 0 1 1.3 2.1C1.3 1.5 1.7 1 2.3 1z"/></svg>
        +1.555.014.2290
      </li>
      <li>
        <svg viewBox="0 0 12 12" aria-hidden="true"><rect x="0.5" y="2" width="11" height="8" rx="1" fill="#e31e24"/><path d="M1 2.6l5 3.8 5-3.8" fill="none" stroke="#0c1631" stroke-width="1"/></svg>
        contact@mesaridgefiber.com
      </li>
      <li>
        <svg viewBox="0 0 12 12" aria-hidden="true"><circle cx="6" cy="6" r="5.2" fill="#e31e24"/><path d="M0.8 6h10.4M6 0.8c-2.2 2.8-2.2 7.6 0 10.4M6 0.8c2.2 2.8 2.2 7.6 0 10.4" fill="none" stroke="#0c1631" stroke-width="0.8"/></svg>
        www.mesaridgefiber.com
      </li>
    </ul>
    <div class="divider"></div>
    <h2 class="services-label">our services</h2>
    <ul class="services-list">
      <li>Home Builders</li>
      <li>Home Owners</li>
      <li>Plumbing Wholesalers</li>
    </ul>
  </div>
</section>

<section class="card card--front" aria-label="Business card, brand side">
  <div class="brand-name">
    <div class="brand-main">MESA RIDGE</div>
    <div class="brand-sub">FIBERGLASS</div>
  </div>
  <p class="tagline">Quality Craftsmanship Today</p>
</section>

</body>
</html>
```